Bartley's Harbor Grill (New Website Design)

I want an upgraded, modern, sleek, tasteful website that is easily updated internally. Our current website can be viewed at www.bartleysharborgrill.example

Target Market(s)

Dining Customers

Industry/Entity Type

Restaurant / Hospitality

Coding

Coded - Design and coding required

Number of Pages Required

4 page

Requirements
Must have
• Modern, artful, sleek.. while maintaining a little vintage Cape Cod

```html
<!DOCTYPE html>
<html lang="en">
<head>
<meta charset="utf-8">
<title>Bartley's Harbor Grill</title>
<link rel="stylesheet" href="https://fonts.googleapis.com/css2?family=Great+Vibes&family=Montserrat:wght@400;500;600&display=swap">
<style>
:root{
  --teal:#22343a;
  --teal-deep:#17262b;
  --navy:#1f3540;
  --red:#e0402a;
  --red-dark:#b8301f;
  --wood:#5a3a22;
  --wood-dark:#3e2615;
  --white:#ffffff;
  --ink:#2a2a2a;
}
*{margin:0;padding:0;box-sizing:border-box}
html,body{width:1200px;height:2967px;overflow:hidden;background:var(--white)}
body{position:relative;font-family:'Montserrat',sans-serif;color:var(--ink)}
.abs{position:absolute}
.script{font-family:'Great Vibes',cursive;font-weight:400;white-space:nowrap}

/* hero */
.sidebar{left:0;top:0;width:329px;height:601px;background:linear-gradient(160deg,#6b4529 0%,var(--wood) 45%,var(--wood-dark) 100%)}
.brand-mark{left:0;width:329px;top:62px;text-align:center;color:var(--white);font-family:'Montserrat',sans-serif;font-weight:600;font-size:22px;letter-spacing:2px;line-height:1.3}
.side-nav{left:0;width:329px;top:224px;list-style:none;text-align:center}
.side-nav li{height:48.6px;color:var(--white);font-size:16px;font-weight:500;letter-spacing:.3px}
.hero-stage{left:329px;top:0;width:871px;height:601px;background:radial-gradient(circle at 50% 50%,#3a3a3c 0%,#253538 45%,#1a2a2e 75%,#3a2328 100%)}
.hero-title{left:329px;width:871px;top:36px;text-align:center;color:var(--white);font-size:58px}
.hero-plate{left:584px;top:121px;width:362px;height:362px;border-radius:50%;background:radial-gradient(circle,#8fb75a 0%,#d9a56a 45%,#ececec 72%,#d8d8d8 100%)}
.hero-sub{left:329px;width:871px;top:496px;text-align:center;color:var(--white);font-size:58px}

/* about */
.about-photo{left:158px;top:697px;width:350px;height:438px;border-radius:50%;border:3px solid var(--navy);background:radial-gradient(ellipse at 50% 45%,#e9a24a 0%,#c9472a 45%,#2b2b2b 85%)}
.ribbon{position:absolute}
.ribbon-tail{position:absolute;background:var(--red-dark)}
.ribbon-body{position:absolute;background:var(--red);color:var(--white);text-align:center;font-family:'Great Vibes',cursive;white-space:nowrap}
.welcome-title{left:660px;top:758px;color:var(--navy);font-size:50px}
.welcome-copy{left:661px;top:843px;width:420px;font-size:15.5px;line-height:35px;color:#222}

/* menus */
.menus-band{left:0;top:1261px;width:1200px;height:576px;background:var(--teal)}
.section-title{left:0;width:1200px;text-align:center;font-size:50px}
.menus-title{top:1318px;color:var(--white)}
.menu-photo{top:1426px;width:256px;height:310px;border-radius:50%;border:3px solid var(--white)}
.gallery-title{top:1916px;color:var(--navy)}

/* footer */
.footer{left:0;top:2562px;width:1200px;height:405px;background:var(--teal)}
.footer-brand{left:0;width:1200px;top:2640px;text-align:center;color:var(--white);font-weight:600;font-size:22px;letter-spacing:2px;line-height:1.3}
.footer-nav{left:0;width:1200px;top:2787px;text-align:center;list-style:none;font-size:12.5px;font-weight:600;color:var(--white)}
.footer-nav li{display:inline-block;margin:0 11px}
.contact-icon{width:38px;height:38px;border-radius:50%;border:1.5px solid var(--white);display:flex;align-items:center;justify-content:center}
.contact-text{color:var(--white);font-size:12.5px;font-weight:600;white-space:nowrap}
.copyright{left:0;width:1200px;top:2911px;text-align:center;color:var(--white);font-size:12.5px;font-weight:600}
</style>
</head>
<body>

<!-- hero -->
<div class="abs sidebar" role="img" aria-label="Dark weathered wood texture"></div>
<div class="abs brand-mark">BARTLEY'S<br>HARBOR GRILL</div>
<ul class="abs side-nav">
  <li>ORDER ONLINE</li><li>OUR MENUS</li><li>SEAFOOD MARKETPLACE</li><li>GIFT CARDS</li><li>ABOUT US</li><li>SIGN IN</li><li>BECOME A VIP</li>
</ul>
<div class="abs hero-stage" role="img" aria-label="Dark teal and burgundy swirl backdrop"></div>
<div class="abs hero-title script">Bartley's</div>
<div class="abs hero-plate" role="img" aria-label="Plate of grilled chicken salad with tomatoes and cucumber"></div>
<div class="abs hero-sub script">Restaurant &amp; Market</div>

<!-- about -->
<div class="abs about-photo" role="img" aria-label="Linguine with tomato sauce and grated cheese"></div>
<div class="ribbon" style="left:69px;top:1077px;width:553px;height:86px">
  <div class="ribbon-tail" style="left:0;top:0;width:50px;height:54px;clip-path:polygon(0 0,100% 0,100% 100%,12% 100%,22% 50%)"></div>
  <div class="ribbon-tail" style="right:0;top:0;width:50px;height:54px;clip-path:polygon(0 0,100% 0,88% 50%,100% 100%,0 100%)"></div>
  <div class="ribbon-body" style="left:31px;top:16px;width:491px;height:70px;line-height:70px;font-size:38px">About Bartley's Harbor Grill</div>
</div>
<div class="abs welcome-title script">Welcome to Bartley's</div>
<p class="abs welcome-copy">Established in 1938, Bartley's Restaurant offers classic Cape Cod fare featuring fresh seafood and creative comfort cuisine. Our comfortable atmosphere includes a lively pub, two fireplace dining rooms, and a Seafood Market with takeout. Located in the charming seaside village of Wexley, Bartley's strives to please each guest with the best dining experience possible.</p>

<!-- menus -->
<div class="abs menus-band"></div>
<svg class="abs" style="left:0;top:1252px" width="1200" height="14" aria-hidden="true"><polygon fill="#22343a" points="0,14 0,7 40,4 80,8 130,3 170,6 220,2 270,7 320,4 370,8 420,3 470,6 520,2 570,7 620,4 670,8 720,3 770,6 820,2 870,7 920,4 970,8 1020,3 1070,6 1120,2 1160,7 1200,4 1200,14"/></svg>
<svg class="abs" style="left:0;top:1833px" width="1200" height="14" aria-hidden="true"><polygon fill="#22343a" points="0,0 1200,0 1200,8 1150,5 1100,10 1050,6 1000,11 950,5 900,9 850,4 800,10 750,6 700,11 650,5 600,9 550,4 500,10 450,6 400,11 350,5 300,9 250,4 200,10 150,6 100,11 50,5 0,9"/></svg>
<div class="abs section-title script menus-title">Our Menus</div>

<div class="abs menu-photo" style="left:128px;background:radial-gradient(ellipse at 50% 65%,#b5482a 0%,#6a2a18 45%,#1b2234 90%)" role="img" aria-label="Grilled kebabs with peppers"></div>
<div class="abs menu-photo" style="left:472px;background:radial-gradient(ellipse at 50% 55%,#c9a07a 0%,#8a6a4a 50%,#3f3a2e 95%)" role="img" aria-label="Shared table of dinner dishes"></div>
<div class="abs menu-photo" style="left:816px;background:radial-gradient(ellipse at 50% 60%,#f1c97a 0%,#d9d0e0 50%,#7f8fc0 95%)" role="img" aria-label="Kids pancakes with strawberries and blueberries"></div>

<div class="ribbon" style="left:121px;top:1688px;width:270px;height:64px">
  <div class="ribbon-tail" style="left:0;top:0;width:34px;height:40px;clip-path:polygon(0 0,100% 0,100% 100%,12% 100%,24% 50%)"></div>
  <div class="ribbon-tail" style="right:0;top:0;width:34px;height:40px;clip-path:polygon(0 0,100% 0,76% 50%,88% 100%,0 100%)"></div>
  <div class="ribbon-body" style="left:23px;top:10px;width:224px;height:54px;line-height:54px;font-size:30px">Daily Special</div>
</div>
<div class="ribbon" style="left:465px;top:1688px;width:270px;height:64px">
  <div class="ribbon-tail" style="left:0;top:0;width:34px;height:40px;clip-path:polygon(0 0,100% 0,100% 100%,12% 100%,24% 50%)"></div>
  <div class="ribbon-tail" style="right:0;top:0;width:34px;height:40px;clip-path:polygon(0 0,100% 0,76% 50%,88% 100%,0 100%)"></div>
  <div class="ribbon-body" style="left:23px;top:10px;width:224px;height:54px;line-height:54px;font-size:30px">Dinner Menu</div>
</div>
<div class="ribbon" style="left:809px;top:1688px;width:270px;height:64px">
  <div class="ribbon-tail" style="left:0;top:0;width:34px;height:40px;clip-path:polygon(0 0,100% 0,100% 100%,12% 100%,24% 50%)"></div>
  <div class="ribbon-tail" style="right:0;top:0;width:34px;height:40px;clip-path:polygon(0 0,100% 0,76% 50%,88% 100%,0 100%)"></div>
  <div class="ribbon-body" style="left:23px;top:10px;width:224px;height:54px;line-height:54px;font-size:30px">Kids Menu</div>
</div>

<!-- gallery -->
<div class="abs section-title script gallery-title">Our Gallery</div>
<div class="abs" style="left:112px;top:2035px;width:312px;height:201px;background:linear-gradient(135deg,#f0b020 0%,#c98a3a 45%,#f2f2ee 100%)" role="img" aria-label="Squash soup with toasted croutons"></div>
<div class="abs" style="left:445px;top:2035px;width:310px;height:201px;background:linear-gradient(135deg,#6f9a3a 0%,#a8c77a 45%,#d9a0b0 100%)" role="img" aria-label="Garden salad with cucumber and red onion"></div>
<div class="abs" style="left:777px;top:2035px;width:311px;height:201px;background:linear-gradient(180deg,#3a3a3c 0%,#8a3a4a 55%,#c9a0a8 100%)" role="img" aria-label="Berry cocktail garnished with blueberries and basil"></div>
<div class="abs" style="left:112px;top:2266px;width:198px;height:202px;background:linear-gradient(135deg,#0f8a5a 0%,#1fc07a 55%,#b8e0c8 100%)" role="img" aria-label="Green cocktail"></div>
<div class="abs" style="left:339px;top:2266px;width:523px;height:202px;background:linear-gradient(100deg,#2a1a20 0%,#c03a5a 45%,#e8c0c8 75%,#9ac43a 100%)" role="img" aria-label="Sugar-rimmed pink drink with lime wedge"></div>
<div class="abs" style="left:886px;top:2266px;width:202px;height:202px;background:linear-gradient(135deg,#e0b060 0%,#b0782a 55%,#6a4218 100%)" role="img" aria-label="Fried clams with fries and coleslaw"></div>

<!-- footer -->
<div class="abs footer"></div>
<svg class="abs" style="left:0;top:2552px" width="1200" height="14" aria-hidden="true"><polygon fill="#22343a" points="0,14 0,6 50,3 100,8 150,4 200,9 250,3 300,7 350,2 400,8 450,4 500,9 550,3 600,7 650,2 700,8 750,4 800,9 850,3 900,7 950,2 1000,8 1050,4 1100,9 1150,3 1200,6 1200,14"/></svg>
<div class="abs footer-brand">BARTLEY'S<br>HARBOR GRILL</div>
<ul class="abs footer-nav">
  <li>ORDER ONLINE</li><li>OUR MENUS</li><li>SEAFOOD MARKETPLACE</li><li>GIFT CARDS</li><li>ABOUT US</li><li>SIGN IN</li><li>BECOME A VIP</li>
</ul>
<div class="abs contact-icon" style="left:288px;top:2837px">
  <svg width="14" height="18" viewBox="0 0 14 18" aria-hidden="true"><path d="M7 0C3.1 0 0 3.1 0 7c0 5 7 11 7 11s7-6 7-11c0-3.9-3.1-7-7-7z" fill="#fff"/><circle cx="7" cy="7" r="2.6" fill="#22343a"/></svg>
</div>
<div class="abs contact-text" style="left:352px;top:2849px">WEXLEY, 418 HARBOR RD, WEXLEY, MA 02699</div>
<div class="abs contact-icon" style="left:755px;top:2837px">
  <svg width="16" height="16" viewBox="0 0 24 24" aria-hidden="true"><path fill="#fff" d="M6.6 10.8a15.1 15.1 0 0 0 6.6 6.6l2.2-2.2a1 1 0 0 1 1-.25 11.4 11.4 0 0 0 3.6.57 1 1 0 0 1 1 1V20a1 1 0 0 1-1 1A17 17 0 0 1 3 4a1 1 0 0 1 1-1h3.5a1 1 0 0 1 1 1c0 1.25.2 2.45.57 3.57a1 1 0 0 1-.25 1z"/></svg>
</div>
<div class="abs contact-text" style="left:814px;top:2849px">(555) 014-2290</div>
<div class="abs copyright">@2024 COPYRIGHTS - ALL RIGHTS RESERVED</div>

</body>
</html>
```